BrightPlacely.com Wordpress Theme

Hi,

I am looking for a new theme for my wordpress site. The site looks average at the moment and needs a boost. I want to have a better user experience for publishers and advertisers and the proposition for each needs to be clear with better links to registration for both.

Publisher and Advertiser sign up buttons should be on the home page.

I am leaving the brief open save I request that you use green colours on the template.

I want room to be able to add more tabs on the top level if we introduce a blog or other services.

The layout needs to be solid and please work with the copy that's already there.

see http://brightplacely.example

I am looking forward to reviewing your ideas and designs.
Updates

The button to carbon neutral cert I am going to want to make smaller and put it in the bottom of the site.

Do not go down the too fluffy green route with windmills and fuzzy clouds. I am looking for something simple, professional but also organic with a bit of zest to it. 

We are not a niche player serving ads to green only site with green only ads. We simply neutralise the effect of online advertising campaigns.

Some decent images in the header on rotation could work I am not sure. I think these would have to be abstract and largely if not totally green in colour.

Target Market(s)

BrightPlacely.com is an online ad network. Our targets are publishers and advertisers. We bring them together through providing ad serving to the network we have built on behalf of our advertisers.

Advertisers are agencys, brands, large companies looking to sell online or create awareness of the brand.

Requirements
Must have
• Please keep the site clean and use green and white
• Call to action to both publishers and advertisers to join (buttons on home page)

```html
<!DOCTYPE html>
<html lang="en">
<head>
<meta charset="utf-8">
<title>BrightPlacely.com</title>
<link rel="stylesheet" href="https://fonts.googleapis.com/css2?family=Didact+Gothic&family=Open+Sans:wght@400;600;700&display=swap">
<style>
:root{
  --green:#2f8a3d;
  --green-dark:#1c6a2c;
  --green-deep:#15592a;
  --green-light:#44a24f;
  --green-text:#1f7a33;
  --ink:#222;
  --grey-line:#d6d6d6;
  --row-bg:#eef0ee;
  --white:#fff;
}
*{box-sizing:border-box;margin:0;padding:0}
html,body{width:929px;height:1200px;overflow:hidden}
body{position:relative;background:linear-gradient(#eeeeee 0,#ffffff 140px);font-family:"Open Sans",sans-serif;color:var(--ink)}
.abs{position:absolute}

.brand{left:40px;top:30px;font:700 34px/46px "Open Sans",sans-serif;color:var(--green-text);letter-spacing:-.5px}
.search{left:697px;top:38px;width:192px;height:23px;display:flex;border:1px solid #ccc;background:var(--white)}
.search span{flex:1;font-size:10px;color:#aaa;padding:5px 5px}
.search b{width:32px;background:var(--green);display:flex;align-items:center;justify-content:center}

.nav{left:40px;top:94px;width:849px;height:27px;background:linear-gradient(var(--green-light),var(--green-dark));box-shadow:0 1px 3px rgba(0,0,0,.3)}
.nav a{position:absolute;top:0;line-height:27px;font:700 12px/27px "Open Sans",sans-serif;color:var(--white);text-decoration:none;transform:translateX(-50%)}
.nav i{position:absolute;top:0;width:1px;height:27px;background:rgba(255,255,255,.35)}

.hero{left:40px;top:134px;width:849px;height:294px;border:1px solid var(--grey-line);background:linear-gradient(#fafafa,#ececec)}
.slide-frame{left:57px;top:146px;width:581px;height:269px;background:var(--white);box-shadow:0 1px 4px rgba(0,0,0,.25)}
.slide{left:68px;top:156px;width:560px;height:248px;background:linear-gradient(135deg,var(--green-light),var(--green-dark))}
.slide-photo{left:76px;top:160px;width:290px;height:244px;background:linear-gradient(var(--green-light),#2c6e35)}
.slide-menu{left:385px;top:176px}
.slide-menu li{list-style:none;font:22px/30.5px "Didact Gothic",sans-serif;color:var(--white)}
.slide-menu li:first-child{border-bottom:1px solid rgba(255,255,255,.5);width:213px}
.signup{left:385px;top:323px;width:131px;height:42px;border:3px solid #e8e8e8;background:var(--green);font:700 20px/36px "Open Sans",sans-serif;color:var(--white);text-align:center}
.dots{left:548px;top:381px;width:81px;height:23px;background:rgba(255,255,255,.35);border-radius:10px 0 0 0}
.dots i{position:absolute;top:6px;width:11px;height:11px;border-radius:50%;background:#e4e4e4;box-shadow:inset 0 1px 2px rgba(0,0,0,.3)}

.hero-side h2{left:662px;top:164px;font:400 21px/28px "Didact Gothic",sans-serif;color:var(--green-text)}
.hero-side p{left:660px;top:196px;width:215px;font-size:10.5px;line-height:15.2px}
.read-more{left:676px;top:330px;width:165px;height:40px;border:1px solid #bbb;border-radius:4px;background:linear-gradient(#fff,#e7e7e7);font:16px/38px "Didact Gothic",sans-serif;color:#666;padding-left:24px}
.read-more i{position:absolute;right:0;top:4px;width:36px;height:30px;border-left:1px solid #ccc;display:flex;align-items:center;justify-content:center}

.welcome{left:40px;top:442px;font:400 26px/36px "Didact Gothic",sans-serif;color:var(--green-text)}
.copy{left:40px;width:525px;font-size:10.5px;line-height:15.2px}
.copy b{color:var(--green-text);font-weight:600}
.features{left:40px;top:561px;width:512px}
.features li{list-style:none;position:relative;height:20.2px}
.features span{position:absolute;left:25px;top:0;width:487px;height:14px;background:var(--row-bg);font:600 10.5px/14px "Open Sans",sans-serif;color:var(--green-text);padding-left:6px;letter-spacing:.2px}
.features svg{position:absolute;left:0;top:2px}

.cta{width:237px;height:111px;border:1px solid var(--grey-line);background:var(--white);left:653px}
.cta-inner{position:absolute;left:9px;top:9px;width:218px;height:93px;background:linear-gradient(var(--green-light),var(--green-dark));color:var(--white);padding:5px 8px}
.cta h3{font:400 25px/28px "Didact Gothic",sans-serif}
.cta p{font-size:10.5px;line-height:12.5px;margin-top:2px}
.cta b{position:absolute;right:0;bottom:0;width:99px;height:24px;background:#151515;font:700 11px/24px "Open Sans",sans-serif;text-align:center}

.footer{left:0;top:897px;width:929px;height:264px;background:linear-gradient(var(--green-light),var(--green-dark))}
.footer h4{position:absolute;top:22px;width:157px;font:400 16px/20px "Didact Gothic",sans-serif;color:var(--white);border-bottom:1px solid rgba(255,255,255,.25);padding-bottom:2px}
.footer ul,.footer p{position:absolute;top:60px;font-size:9.5px;line-height:15.2px;color:var(--white);list-style:none;letter-spacing:.2px}
.footer li::before{content:"› ";font-weight:700}
.badge{left:722px;top:1052px;width:151px;height:74px;background:var(--white);border:1px solid #ccc;box-shadow:0 1px 3px rgba(0,0,0,.3)}
.badge i{position:absolute;left:9px;top:10px;width:131px;height:52px;background:linear-gradient(#f4f9f1,#dfeed9)}
.bottom-bar{left:0;top:1161px;width:929px;height:39px;background:linear-gradient(var(--green-light),var(--green));font:700 9.5px/39px "Open Sans",sans-serif;color:var(--white);padding:0 43px;display:flex;justify-content:space-between;letter-spacing:.4px}
</style>
</head>
<body>

<div class="abs brand">BrightPlacely.com</div>
<div class="abs search"><span>Search..</span><b><svg width="14" height="14" viewBox="0 0 14 14"><circle cx="6" cy="6" r="4" fill="none" stroke="#fff" stroke-width="2"/><line x1="9" y1="9" x2="13" y2="13" stroke="#fff" stroke-width="2"/></svg></b></div>

<nav class="abs nav">
  <a style="left:57px">Home</a><i style="left:110px"></i>
  <a style="left:171px">Advertisers</a><i style="left:237px"></i>
  <a style="left:297px">Publishers</a><i style="left:357px"></i>
  <a style="left:412px">Referral</a><i style="left:465px"></i>
  <a style="left:527px">Offsetting</a><i style="left:584px"></i>
  <a style="left:651px">Contact Us</a>
</nav>

<div class="abs hero"></div>
<div class="abs slide-frame"></div>
<div class="abs slide"></div>
<div class="abs slide-photo" role="img" aria-label="Photo of a man in a suit holding a blank advertising sign"></div>
<ul class="abs slide-menu">
  <li>Advertiser Information</li>
  <li>Advertiser Login</li>
  <li>Advertiser Sign Up</li>
  <li>Advertising Formats</li>
</ul>
<div class="abs signup">Sign Up »</div>
<div class="abs dots"><i style="left:7px"></i><i style="left:33px"></i><i style="left:59px"></i></div>

<div class="hero-side">
  <h2 class="abs">ADVERTISERS</h2>
  <p class="abs">BrightPlacely.com can provide you access to over a billion impressions a month to drive quality traffic to your website to convert. Our advanced advertising technology enables a very high degree of targeting to improve the performance of your campaigns.</p>
  <div class="abs read-more">Read More<i><svg width="10" height="14" viewBox="0 0 10 14"><path d="M2 1l6 6-6 6" fill="none" stroke="#777" stroke-width="3"/></svg></i></div>
</div>

<h1 class="abs welcome">Welcome to Our Website</h1>
<p class="abs copy" style="top:490px"><b>BrightPlacely.com</b> is a contextual advertising network and ad exchange that brings together publishers of high quality content with advertisers, enabling them to reach their target market whilst publishers monetize their sites through advertising that's in keeping with their sites.</p>

<ul class="abs features">
  <li><svg width="18" height="10" viewBox="0 0 18 10"><path d="M1 1l4 4-4 4M7 1l4 4-4 4M13 1l4 4-4 4" fill="none" stroke="#1f7a33" stroke-width="2"/></svg><span>Hundreds of millions of monthly ad impressions across ours and our partner networks</span></li>
  <li><svg width="18" height="10" viewBox="0 0 18 10"><path d="M1 1l4 4-4 4M7 1l4 4-4 4M13 1l4 4-4 4" fill="none" stroke="#1f7a33" stroke-width="2"/></svg><span>170+ content channels to target</span></li>
  <li><svg width="18" height="10" viewBox="0 0 18 10"><path d="M1 1l4 4-4 4M7 1l4 4-4 4M13 1l4 4-4 4" fill="none" stroke="#1f7a33" stroke-width="2"/></svg><span>B2B &amp; B2C traffic</span></li>
  <li><svg width="18" height="10" viewBox="0 0 18 10"><path d="M1 1l4 4-4 4M7 1l4 4-4 4M13 1l4 4-4 4" fill="none" stroke="#1f7a33" stroke-width="2"/></svg><span>Geo Targeting</span></li>
  <li><svg width="18" height="10" viewBox="0 0 18 10"><path d="M1 1l4 4-4 4M7 1l4 4-4 4M13 1l4 4-4 4" fill="none" stroke="#1f7a33" stroke-width="2"/></svg><span>Behavioural Targeting</span></li>
  <li><svg width="18" height="10" viewBox="0 0 18 10"><path d="M1 1l4 4-4 4M7 1l4 4-4 4M13 1l4 4-4 4" fill="none" stroke="#1f7a33" stroke-width="2"/></svg><span>Re-Targeting</span></li>
  <li><svg width="18" height="10" viewBox="0 0 18 10"><path d="M1 1l4 4-4 4M7 1l4 4-4 4M13 1l4 4-4 4" fill="none" stroke="#1f7a33" stroke-width="2"/></svg><span>Real Time Campaign Tracking &amp; Reporting</span></li>
  <li><svg width="18" height="10" viewBox="0 0 18 10"><path d="M1 1l4 4-4 4M7 1l4 4-4 4M13 1l4 4-4 4" fill="none" stroke="#1f7a33" stroke-width="2"/></svg><span>ROI tracking</span></li>
</ul>

<p class="abs copy" style="top:733px"><b>BrightPlacely.com</b> collates high quality content across a range of specialist and generalist websites and blogs and equips advertisers with the tools to target visitors and optimize campaign performance.</p>
<p class="abs copy" style="top:794px">As you may have guested by our name <b>BrightPlacely.com</b> is both responsible and ethical.</p>
<p class="abs copy" style="top:824px">100% of the ads we serve are carbon offset meaning that you can feel good in the fact that the environmental impact of your advertising campaign has been neutralized.</p>

<div class="abs cta" style="top:490px"><div class="cta-inner"><h3>ADVERTISER?</h3><p>BrightPlacely.com can provide you access to over a billion impressions a month to drive...</p><b>Register Now ›</b></div></div>
<div class="abs cta" style="top:614px"><div class="cta-inner"><h3>PUBLISHER?</h3><p>BrightPlacely.com can provide you access to over a billion impressions a month to drive...</p><b>Register Now ›</b></div></div>

<footer class="abs footer">
  <h4 style="left:43px">Pages</h4>
  <ul style="left:43px">
    <li>Contact</li><li>Offsetting</li><li>Referral</li><li>Publishers</li><li>Ad Formats</li><li>Publisher Registration</li><li>Publisher Agreement</li><li>Advertisers</li><li>Ad Formats</li><li>Testimonials</li><li>Advertiser Registration</li><li>Advertiser Agreement</li>
  </ul>
  <h4 style="left:270px">Advertisers</h4>
  <p style="left:269px;width:160px">BrightPlacely.com can provide you access to over a billion impressions a month to drive quality traffic to your website to convert. Our advanced advertising technology enables a very high degree of targeting to improve the performance of your campaigns.</p>
  <h4 style="left:498px">Publishshers</h4>
  <p style="left:497px;width:160px">BrightPlacely.com offers publishers to the opportunity to earn more income through text (inline text links) or by displaying targeted contextual advertising banner ads on their websites or blogs.</p>
  <h4 style="left:721px">Useful Info</h4>
  <ul style="left:721px">
    <li>Contact Us</li><li>Terms &amp; Conditions : Advertisers</li><li>Terms &amp; Conditions : Publishers</li><li>User Guide: Advertisers</li><li>User Guide: Publishers</li>
  </ul>
</footer>
<div class="abs badge" role="img" aria-label="Carbon neutral certificate badge"><i></i></div>

<div class="abs bottom-bar"><span>Copyright BrightPlacely.com Ltd 2010</span><span>Home | Advertisers | Publishers | Contact Us</span></div>

</body>
</html>
```